A colorful, playful, nerdy, creative logo for a business analytics and marketing analytics company.

We need a logo and website design for a new company based in Florida called Brightfold Pattern Works Collective. We provide marketing, consumer and business insights through the use of market research, business analytics and marketing analytics. We are a collection of several individuals each with specific expertise and come together to provide the best possible insights about their consumers/guests/customers. We would like to see a design that uses colors that show a free spirit but deeply rooted in analytics " a super nerd " Along those steps, we would like to see either a playful, nerdy, creative logo or one that includes the full or partial name of the company. We have simplified our "brand" by saying when you initially start with us you may have several questions "?" through the process of learning about your consumers/brand ">" incredible solutions, strategies are developed "!" So something like a ?>! symbol would be interesting. Although the name of the company sounds very complex and very long to write, we would be interested in thoughtful ways of shorting the name or incorporating into the final logo design

Target Market(s)

Business or organizations that currently do not have an analytics/research function

Industry/Entity Type

Business

Contact Information for Business Card

Incorporate final logo and colors font. In the past, I have used a "wordle" website to show 10 common research terms scattered about .. showing them as strength or core competencies.

Logo Text

?>! or Brightfold Pattern Works Collective or BPW Collective

Coding

Coded - Design and coding required

Number of Pages Required

4 page

Font styles to use
Sans Serif
Decorative

Requirements
Must have
• The project must communicate analytics/scientific. It must we unique but not unique for the sack of being unique.
• It must either be a logo or a simple way to communicate the company name Brightfold Pattern Works Collective
Nice to have
• Again incorporating the symbols ?>! in that order. Showing confusion to gaining insights and then developing incredible solutions that are used to effect consumer behavior.
• Look to CPG ( consumer package goods) industry to input
Should not have
• I am pretty open to suggestions.

```html
<!DOCTYPE html>
<html lang="en">
<head>
<meta charset="utf-8">
<title>BPWC — Brightfold Pattern Works Collective</title>
<link rel="stylesheet" href="https://fonts.googleapis.com/css2?family=Jost:wght@300;400;500&family=Open+Sans:wght@400;600;700&display=swap">
<style>
:root{
  --blue:#1466c0;
  --blue-dark:#0d56a8;
  --footer:#0b5fbd;
  --orange:#f4a21c;
  --pink:#e2257c;
  --ink:#2b2b2b;
  --muted:#666;
  --grey-bg:#f1f1f1;
  --line:#cfcfcf;
  --white:#fff;
}
*{margin:0;padding:0;box-sizing:border-box}
html,body{width:1200px;height:4072px;overflow:hidden}
body{position:relative;background:var(--white);font-family:"Open Sans",Arial,sans-serif;color:var(--ink)}
.abs{position:absolute}
.band{position:absolute;left:0;width:1200px}
.heading{font-family:"Jost",Arial,sans-serif;font-weight:400;color:var(--blue);font-size:31px;letter-spacing:1px;text-align:center;width:1200px;left:0}
.rule{position:absolute;left:570px;width:60px;height:2px;background:var(--line)}
.btn{position:absolute;display:flex;align-items:center;justify-content:center;font-size:12px;text-transform:uppercase;letter-spacing:.5px;border:1.5px solid;background:var(--white)}
.copy{font-size:12.5px;line-height:21px;color:var(--muted)}

/* header */
.logo{font-family:"Jost",Arial,sans-serif;font-weight:300;color:var(--blue);font-size:46px;letter-spacing:1px;left:128px;top:18px;line-height:56px}
.nav{font-size:13px;top:38px;color:var(--ink);text-transform:uppercase}
.btn-try{left:842px;top:33px;width:114px;height:32px;color:var(--blue);border-color:var(--blue)}
.btn-login{left:977px;top:33px;width:90px;height:32px;color:var(--white);background:var(--blue);border-color:var(--blue);font-weight:600;gap:8px}

/* hero */
.hero{top:95px;height:538px;background:linear-gradient(120deg,#c9d3db 0%,#8f9fac 45%,#4f5f6e 100%)}
.hero-shade{top:95px;height:538px;background:linear-gradient(0deg,rgba(0,0,0,.45),rgba(0,0,0,0) 45%)}
.hero-title{left:128px;top:478px;color:var(--white);font-weight:700;font-size:34px;line-height:46px}
.hero-title .upper{text-transform:uppercase}
.hero-arrow{width:40px;height:50px;background:rgba(40,40,40,.75);top:340px;display:flex;align-items:center;justify-content:center}
.dot{position:absolute;width:9px;height:9px;border-radius:50%;background:var(--white)}
.dot.ring{background:transparent;border:1.5px solid var(--white)}

/* services */
.svc-title{font-size:14px;text-transform:uppercase;width:300px;text-align:center;top:990px}
.svc-copy{width:240px;text-align:center;top:1024px}

/* welcome */
.welcome{top:1385px;height:551px;background:var(--grey-bg)}
.skyline{left:470px;top:1690px;width:730px;height:246px;background:linear-gradient(0deg,#dcdcdc,#ebebeb 70%,rgba(241,241,241,0))}
.tablet{left:692px;top:1447px;width:340px;height:436px;border-radius:20px;background:linear-gradient(160deg,#f4f7fa 0%,#cfe6f3 55%,#f5c3d2 100%)}
.feat-icon{width:62px;height:62px;border-radius:50%;border:1.5px solid var(--blue);background:var(--white);display:flex;align-items:center;justify-content:center}
.feat-title{font-size:13px;font-weight:600;text-transform:uppercase;left:250px}
.feat-copy{font-size:11.5px;color:var(--muted);left:250px}

/* help */
.help-title{font-size:13.5px;text-transform:uppercase;top:2183px}
.help-copy{width:225px;text-align:justify;top:2232px}

/* testimonials */
.testi{top:2498px;height:521px;background:var(--grey-bg)}
.quote{top:2693px;height:190px;background:var(--blue);color:var(--white);font-size:12px;line-height:19px;padding:20px 24px}
.quote .who{font-size:11px;font-weight:700;margin-top:12px}
.quote .who span{font-weight:400}
.avatar{width:80px;height:80px;border-radius:50%;background:linear-gradient(135deg,#bcbcbc,#7d7d7d);top:2748px}

/* stats */
.stats{top:3380px;height:272px;background:var(--grey-bg)}
.stat{top:3380px;width:300px;height:272px;text-align:center}
.stat-num{font-family:"Jost",Arial,sans-serif;font-weight:300;color:var(--blue);font-size:42px;position:absolute;top:118px;width:300px}
.stat-label{position:absolute;top:186px;width:300px;font-size:13px;line-height:24px;text-transform:uppercase;color:var(--ink)}
.stat-divider{position:absolute;top:3380px;width:1px;height:272px;background:#dedede}

/* footer */
.footer{top:3652px;height:420px;background:var(--footer);color:var(--white)}
.f-logo{font-family:"Jost",Arial,sans-serif;font-weight:300;font-size:58px;left:130px;top:3770px;color:var(--white)}
.f-head{font-size:12px;font-weight:700;text-transform:uppercase;top:3706px;color:var(--white)}
.f-text{font-size:12px;color:var(--white);line-height:18px}
.f-icon{width:32px;height:32px;border-radius:50%;border:1.5px solid var(--white);display:flex;align-items:center;justify-content:center}
.f-menu{left:638px;top:3748px;font-size:12.5px;line-height:24px;color:var(--white);list-style:none}
.f-input{left:806px;top:3752px;width:261px;height:46px;background:var(--white);color:#333;font-size:13px;display:flex;align-items:center;padding-left:18px;gap:12px}
.f-signup{left:950px;top:3817px;width:117px;height:44px;background:var(--orange);color:var(--white);font-weight:700;font-size:14px;display:flex;align-items:center;justify-content:center;text-transform:uppercase}
.f-rule{left:130px;top:3969px;width:937px;height:1px;background:rgba(255,255,255,.3)}
.social{width:26px;height:26px;border-radius:50%;top:4011px}
</style>
</head>
<body>

<!-- header -->
<div class="abs logo">BPWC</div>
<div class="abs nav" style="left:340px">Solutions</div>
<div class="abs nav" style="left:448px">Services</div>
<div class="abs nav" style="left:543px">Marketing</div>
<div class="abs nav" style="left:652px">Resources</div>
<div class="abs nav" style="left:755px">Contact</div>
<div class="btn btn-try">Try it for free</div>
<div class="btn btn-login"><svg width="11" height="12" viewBox="0 0 11 12"><rect x="1" y="5" width="9" height="7" fill="#fff"/><path d="M3 5V3.5a2.5 2.5 0 0 1 5 0V5" stroke="#fff" stroke-width="1.5" fill="none"/></svg>Login</div>

<!-- hero -->
<div class="band hero" role="img" aria-label="Photo of a presenter showing charts on a board to colleagues around a meeting table"></div>
<div class="band hero-shade"></div>
<div class="abs hero-arrow" style="left:0"><svg width="12" height="18"><path d="M10 2 3 9l7 7" stroke="#fff" stroke-width="2" fill="none"/></svg></div>
<div class="abs hero-arrow" style="left:1160px"><svg width="12" height="18"><path d="M2 2l7 7-7 7" stroke="#fff" stroke-width="2" fill="none"/></svg></div>
<div class="abs hero-title"><div class="upper">Brightfold Pattern</div><div>Works Collective</div></div>
<div class="dot" style="left:535px;top:581px"></div>
<div class="dot ring" style="left:566px;top:581px"></div>
<div class="dot" style="left:598px;top:581px"></div>
<div class="dot" style="left:630px;top:581px"></div>
<div class="dot" style="left:662px;top:581px"></div>

<!-- services -->
<div class="abs heading" style="top:698px">OUR SERVICES</div>
<div class="rule" style="top:768px"></div>

<svg class="abs" style="left:208px;top:838px" width="100" height="100" viewBox="0 0 100 100" fill="none" stroke="#f4a21c" stroke-width="3">
  <circle cx="40" cy="38" r="22"/><path d="M56 54l18 18"/><path d="M32 44v-8M40 44V30M48 44v-12"/><path d="M20 92h64M28 92V72M40 92V78M52 92V70M64 92V76M76 92V66"/>
</svg>
<svg class="abs" style="left:550px;top:838px" width="100" height="100" viewBox="0 0 100 100" fill="none" stroke="#1466c0" stroke-width="3">
  <path d="M10 10v80h84"/><path d="M22 86V64M34 86V56M46 86V60M58 86V46M70 86V38M82 86V26" stroke-dasharray="3 3"/><path d="M18 66l20-14 14 6 16-18 18-16"/><circle cx="86" cy="24" r="3"/>
</svg>
<svg class="abs" style="left:878px;top:838px" width="100" height="100" viewBox="0 0 100 100" fill="none" stroke="#e2257c" stroke-width="3">
  <rect x="38" y="12" width="52" height="40"/><path d="M44 44l12-12 10 6 16-16"/><path d="M64 52v12M54 72l10-8 10 8"/><circle cx="22" cy="46" r="9"/><path d="M8 92V68a14 14 0 0 1 28 0v24M36 66l10-8"/>
</svg>

<div class="abs svc-title" style="left:108px">Market Research</div>
<div class="abs svc-title" style="left:450px">Business Analytics</div>
<div class="abs svc-title" style="left:778px">Marketing Analytics</div>
<div class="abs copy svc-copy" style="left:138px">It is a long established fact that a reader will be distracted by the readable content</div>
<div class="abs copy svc-copy" style="left:480px">It is a long established fact that a reader will be distracted by the readable content</div>
<div class="abs copy svc-copy" style="left:808px">It is a long established fact that a reader will be distracted by the readable content</div>
<div class="btn" style="left:205px;top:1129px;width:108px;height:33px;color:var(--orange);border-color:var(--orange)">Read more</div>
<div class="btn" style="left:546px;top:1129px;width:108px;height:33px;color:var(--blue);border-color:var(--blue)">Read more</div>
<div class="btn" style="left:874px;top:1129px;width:108px;height:33px;color:var(--pink);border-color:var(--pink)">Read more</div>
<svg class="abs" style="left:0;top:1162px" width="1200" height="140" viewBox="0 1162 1200 140" fill="none" stroke-width="2">
  <path d="M259 1162v81h273v44" stroke="#f4a21c"/><circle cx="532" cy="1291" r="6" fill="#f4a21c" stroke="none"/>
  <path d="M600 1162v125" stroke="#1466c0"/><circle cx="600" cy="1291" r="6" fill="#1466c0" stroke="none"/>
  <path d="M928 1162v81H684v44" stroke="#e2257c"/><circle cx="684" cy="1291" r="6" fill="#e2257c" stroke="none"/>
</svg>

<!-- welcome -->
<div class="band welcome"></div>
<div class="abs skyline" role="img" aria-label="Faint city skyline silhouette"></div>
<div class="abs" style="left:157px;top:1442px;display:flex;align-items:baseline;gap:12px">
  <span style="font-size:14px;text-transform:uppercase">Welcome to</span>
  <span style="font-family:'Jost',Arial,sans-serif;font-weight:300;font-size:46px;color:var(--blue)">BPWC</span>
</div>
<div class="abs copy" style="left:157px;top:1516px;width:520px">There are many variations of passages of Lorem Ipsum available, but the majority have suffered alteration in some.</div>

<div class="abs feat-icon" style="left:159px;top:1606px"><svg width="28" height="28" viewBox="0 0 28 28" fill="none" stroke="#1466c0" stroke-width="1.6"><path d="M3 13 25 4l-6 20-6-7z"/><path d="M13 17l12-13"/></svg></div>
<div class="abs feat-title" style="top:1612px">Our Mission</div>
<div class="abs feat-copy" style="top:1637px">It is a long established fact that a reader will be distracted</div>

<div class="abs feat-icon" style="left:159px;top:1707px"><svg width="30" height="28" viewBox="0 0 30 28" fill="none" stroke="#1466c0" stroke-width="1.6"><circle cx="10" cy="9" r="5"/><circle cx="21" cy="11" r="4"/><path d="M2 25a8 8 0 0 1 16 0M16 25a6 6 0 0 1 12 0"/></svg></div>
<div class="abs feat-title" style="top:1713px">Team</div>
<div class="abs feat-copy" style="top:1738px">Contrary to popular belief, Lorem Ipsum</div>

<div class="abs feat-icon" style="left:159px;top:1807px"><svg width="26" height="26" viewBox="0 0 26 26" fill="none" stroke="#1466c0" stroke-width="1.6"><path d="M6 3l4 5-2 3c1 3 4 6 7 7l3-2 5 4-2 3C12 24 2 14 3 5z"/></svg></div>
<div class="abs feat-title" style="top:1813px">Get Support</div>
<div class="abs feat-copy" style="top:1838px">Embarrassing hidden in the middle of text. All the Lorem Ipsum</div>

<div class="abs tablet" role="img" aria-label="Illustration of a tablet displaying the BPWC dashboard with bar and line charts"></div>

<!-- help -->
<div class="abs heading" style="top:2020px">WE'RE HERE TO HELP</div>
<div class="abs copy" style="left:0;width:1200px;text-align:center;top:2084px;font-size:14px">Lorem Ipsum is simply dummy text of the printing</div>

<svg class="abs" style="left:128px;top:2178px" width="50" height="40" viewBox="0 0 50 40" fill="none" stroke="#222" stroke-width="2"><path d="M8 12h32v20H8z"/><path d="M8 12l16 12 16-12"/><path d="M2 16h4M0 22h6M2 28h4"/></svg>
<div class="abs help-title" style="left:198px">Contact Us</div>
<div class="abs copy help-copy" style="left:198px">There are many variations of passages of Lorem Ipsum available, but the majority have suffered alteration.</div>
<div class="btn" style="left:204px;top:2354px;width:120px;height:33px;color:var(--ink);border-color:#555">Get directions</div>

<svg class="abs" style="left:467px;top:2176px" width="50" height="44" viewBox="0 0 50 44" fill="#222"><rect x="18" y="2" width="30" height="22" fill="none" stroke="#222" stroke-width="2.5"/><path d="M26 18l6-6 4 3 6-7" fill="none" stroke="#222" stroke-width="2"/><circle cx="10" cy="14" r="5"/><rect x="4" y="21" width="12" height="21"/><path d="M16 24l10-6" stroke="#222" stroke-width="3"/></svg>
<div class="abs help-title" style="left:538px">One-on-One Training</div>
<div class="abs copy help-copy" style="left:538px">Lorem Ipsum is simply dummy text of the printing and typesetting industry. Lorem Ipsum has been the industry's.</div>
<div class="btn" style="left:544px;top:2354px;width:98px;height:33px;color:var(--ink);border-color:#555">Read more</div>

<svg class="abs" style="left:795px;top:2176px" width="50" height="46" viewBox="0 0 50 46" fill="none" stroke="#222" stroke-width="3"><circle cx="18" cy="26" r="9"/><circle cx="18" cy="26" r="14" stroke-dasharray="5 4" stroke-width="5"/><circle cx="38" cy="12" r="5"/><circle cx="38" cy="12" r="9" stroke-dasharray="4 3" stroke-width="4"/></svg>
<div class="abs help-title" style="left:869px">Self-Help Resources</div>
<div class="abs copy help-copy" style="left:869px">Sed ut perspiciatis unde omnis iste natus error sit voluptatem accusantium dolor emq ue laudantium, totam.</div>
<div class="btn" style="left:874px;top:2354px;width:98px;height:33px;color:var(--ink);border-color:#555">Read more</div>

<!-- testimonials -->
<div class="band testi"></div>
<div class="abs heading" style="top:2557px">WHAT OUR CUSTOMER SAYS</div>
<div class="rule" style="top:2625px"></div>

<div class="abs avatar" style="left:164px" role="img" aria-label="Portrait of Daniel"></div>
<svg class="abs" style="left:252px;top:2776px" width="16" height="24"><path d="M16 0 0 12l16 12z" fill="#1466c0"/></svg>
<div class="abs quote" style="left:266px;width:326px">
  Lorem ipsum dolor sit amet, consectetur adipiscing elit. Facere deleniti enim ut recusandae ipsum inventore ducimus quam ea reprehenderit beatae facilis, voluptatecommodi deserunt magni ipsa.
  <div class="who">DANIEL, <span>ENGLAND</span></div>
</div>

<div class="abs quote" style="left:630px;width:301px">
  But I must explain to you how all this mistaken idea of denouncing pleasure and praising pain was born and I will give you a complete account of the system, and expound the actual teachings of the great.
  <div class="who">MARCO, <span>ENGLAND</span></div>
</div>
<svg class="abs" style="left:931px;top:2776px" width="16" height="24"><path d="M0 0l16 12L0 24z" fill="#1466c0"/></svg>
<div class="abs avatar" style="left:959px" role="img" aria-label="Portrait of Marco"></div>

<div class="dot" style="left:572px;top:2948px;background:#bbb;width:7px;height:7px"></div>
<div class="dot" style="left:588px;top:2948px;background:var(--blue);width:7px;height:7px"></div>
<div class="dot" style="left:604px;top:2948px;background:#bbb;width:7px;height:7px"></div>
<div class="dot" style="left:620px;top:2948px;background:#bbb;width:7px;height:7px"></div>

<!-- get started -->
<div class="abs heading" style="top:3111px">GET STARTED FOR FREE</div>
<div class="abs copy" style="left:0;width:1200px;text-align:center;top:3176px;font-size:14px">There are many variations of passages of Lorem Ipsum available, but the majority have suffered alteration.</div>
<div class="btn" style="left:513px;top:3247px;width:171px;height:44px;color:var(--blue);border-color:var(--blue);font-size:14px;font-weight:600">Sign up now</div>

<!-- stats -->
<div class="band stats"></div>
<div class="stat-divider" style="left:300px"></div>
<div class="stat-divider" style="left:600px"></div>
<div class="stat-divider" style="left:900px"></div>
<div class="abs stat" style="left:26px">
  <svg style="position:absolute;left:135px;top:58px" width="30" height="34" viewBox="0 0 30 34" fill="none" stroke="#1466c0" stroke-width="2.5"><rect x="10" y="2" width="10" height="18" rx="5" fill="#1466c0"/><path d="M5 14a10 10 0 0 0 20 0M15 24v8M9 32h12"/></svg>
  <div class="stat-num">60+</div><div class="stat-label">Inspiring<br>Speakers</div>
</div>
<div class="abs stat" style="left:300px">
  <svg style="position:absolute;left:130px;top:60px" width="40" height="30" viewBox="0 0 40 30" fill="none" stroke="#1466c0" stroke-width="2.5"><path d="M2 10l8-6 8 4 6-4 14 6"/><path d="M6 14l12 12 4-2 4-2 8-8"/><path d="M18 8l-4 6 6 2 6-6"/></svg>
  <div class="stat-num">25+</div><div class="stat-label">Sponsoring<br>Partners</div>
</div>
<div class="abs stat" style="left:600px">
  <svg style="position:absolute;left:130px;top:58px" width="40" height="32" viewBox="0 0 40 32" fill="none" stroke="#1466c0" stroke-width="2.5"><circle cx="14" cy="10" r="6"/><circle cx="28" cy="11" r="5"/><path d="M3 30a11 11 0 0 1 22 0M21 30a9 9 0 0 1 17 0"/></svg>
  <div class="stat-num">12+</div><div class="stat-label">Team<br>Employees</div>
</div>
<div class="abs stat" style="left:874px">
  <svg style="position:absolute;left:132px;top:58px" width="36" height="32" viewBox="0 0 36 32" fill="none" stroke="#1466c0" stroke-width="2.5"><rect x="3" y="9" width="30" height="20"/><path d="M12 9V4h12v5M3 17h30"/></svg>
  <div class="stat-num">156+</div><div class="stat-label">Business<br>Workers</div>
</div>

<!-- footer -->
<div class="band footer"></div>
<div class="abs f-logo">BPWC</div>

<div class="abs f-head" style="left:369px">Contact us</div>
<div class="abs f-icon" style="left:372px;top:3763px"><svg width="12" height="16" viewBox="0 0 12 16"><path d="M6 15S1 9 1 6a5 5 0 0 1 10 0c0 3-5 9-5 9z" fill="#fff"/><circle cx="6" cy="6" r="2" fill="#0b5fbd"/></svg></div>
<div class="abs f-text" style="left:426px;top:3762px">1180 Harbor Palm Way<br>Sarasota, FL 34236</div>
<div class="abs f-icon" style="left:372px;top:3812px"><svg width="14" height="14" viewBox="0 0 26 26"><path d="M6 3l4 5-2 3c1 3 4 6 7 7l3-2 5 4-2 3C12 24 2 14 3 5z" fill="#fff"/></svg></div>
<div class="abs f-text" style="left:426px;top:3819px">555.010.2040</div>
<div class="abs f-icon" style="left:372px;top:3861px"><svg width="14" height="11" viewBox="0 0 14 11"><rect width="14" height="11" fill="#fff"/><path d="M0 0l7 6 7-6" stroke="#0b5fbd" stroke-width="1.5" fill="none"/></svg></div>
<div class="abs f-text" style="left:426px;top:3868px">hello@bpwc.co</div>

<div class="abs f-head" style="left:638px">Menu</div>
<ul class="abs f-menu"><li>Solutions</li><li>Services</li><li>Marketing</li><li>Resources</li><li>Contact</li></ul>

<div class="abs f-head" style="left:806px">Newsletter signup!</div>
<div class="abs f-input"><svg width="14" height="11" viewBox="0 0 14 11" fill="none" stroke="#333" stroke-width="1.3"><rect x=".7" y=".7" width="12.6" height="9.6"/><path d="M.7.7 7 6l6.3-5.3"/></svg>E-mail id</div>
<div class="abs f-signup">Signup!</div>

<div class="abs f-rule"></div>
<div class="abs f-text" style="left:130px;top:4016px;font-size:11px;font-weight:700">FOLLOW US :</div>
<div class="abs social" style="left:218px;background:#3b5fb0"></div>
<div class="abs social" style="left:250px;background:#28a8e6"></div>
<div class="abs social" style="left:286px;background:#e2452c"></div>
<div class="abs f-text" style="left:700px;width:367px;text-align:right;top:4016px;font-size:11px">Copyrights © 2017 All Rights Reserved</div>

</body>
</html>
```